vestra charcoal

We need a package design for a 10 LBS/4.54kg of charcoal bag which will be printed on Kraft paper
the name of the product is Vestra Charcoal we will need a catchy logo for this
The design should have two colors red and any other. Please note that it will be printed on brown kraft paper. It should have our website on it www.vestracharcoal-example.com which should be obvious enough without congesting the design.
The design should not contravene any trademark.
It should feature the following qualities in a neat but catchy way:
100% all natural hardwood lump charcoal
No scrap, no fillers, burns hotter, cleaner and longer
No sparking, Low ash, top quality
Slogan:
...light the smoke flavor.
The design should make up just 40-50% of the paper space
It should have this warning info behind it or at the side
Warning
Carbon monoxide hazard
Burning charcoal inside homes or vehicles can kill you
It emits carbon monoxide which has no odor.
The following should be toked somewhere on the side
Manufactured by:
Kelvaro investment co. Ltd.
12, Tamburi Str. off elvoka Cross rd.
IkeJa lagos, Nigeria.
23419075521
2348159067714
info@vestracharcoal-example.com
Palvetta LLC USA
5027741963
palvet@vestracharcoal-example.com
The following information should be at the back
vestracharcoal is purely made from hardwood. It lights up fast and needs no petroleum starting fluid. It contains no chemicals or additive...just the purest form of charcoal.
Light up instruction: (please develop a diagrammatic representation for this)
1. Roll a full sheet of newspaper into a tube then form it into a donut shape.
2. Build the coals up around the donut shaped newspaper in a pyramid fashion.
3. light the paper in different places and let it go.
Other information will come in later

```html
<!DOCTYPE html>
<html lang="en">
<head>
<meta charset="utf-8">
<title>Vestra Charcoal – 10 LBS Bag Front</title>
<link rel="stylesheet" href="https://fonts.googleapis.com/css2?family=Oswald:wght@500;600;700&display=swap">
<style>
  :root {
    --paper: #ffffff;
    --red: #b52a2c;
    --ink: #231f20;
    --white: #ffffff;
  }
  * { margin: 0; padding: 0; box-sizing: border-box; }
  html, body {
    width: 1200px;
    height: 1020px;
    overflow: hidden;
    background: var(--paper);
  }
  .canvas {
    position: relative;
    width: 1200px;
    height: 1020px;
    background: var(--paper);
  }
  .bag-front {
    position: absolute;
    left: 365px;
    top: 55px;
    width: 470px;
    height: 880px;
  }
  .brand-name {
    position: absolute;
    left: 0;
    top: 90px;
    width: 470px;
    text-align: center;
    font-family: "Oswald", sans-serif;
    font-weight: 500;
    color: var(--ink);
    font-size: 60px;
    line-height: 80px;
    letter-spacing: 1px;
    white-space: nowrap;
  }
  .slogan {
    position: absolute;
    left: 30px;
    top: 268px;
    font-family: "Oswald", sans-serif;
    font-weight: 500;
    font-size: 40px;
    color: var(--red);
    transform: rotate(-8deg);
    transform-origin: left bottom;
    white-space: nowrap;
  }
  .product-claim {
    position: absolute;
    left: 72px;
    top: 372px;
    font-family: "Oswald", sans-serif;
    font-weight: 700;
    font-size: 20px;
    color: var(--ink);
    transform: rotate(-7deg);
    transform-origin: left bottom;
    white-space: nowrap;
  }
  .feature {
    position: absolute;
    height: 42px;
    background: var(--ink);
    color: var(--white);
    font-family: "Oswald", sans-serif;
    font-weight: 600;
    font-size: 21px;
    line-height: 42px;
    text-align: center;
    transform: rotate(-7deg);
    transform-origin: left bottom;
    white-space: nowrap;
  }
  .feature--one   { left: 25px; top: 450px; width: 360px; }
  .feature--two   { left: 60px; top: 503px; width: 310px; }
  .feature--three { left: 25px; top: 556px; width: 325px; }
  .flame-band {
    position: absolute;
    left: 0;
    top: 605px;
    width: 470px;
    height: 275px;
  }
  .net-weight {
    position: absolute;
    left: 255px;
    top: 775px;
    width: 110px;
    text-align: center;
    font-family: "Oswald", sans-serif;
    font-weight: 700;
    color: var(--white);
  }
  .net-weight .lbs {
    display: block;
    font-size: 28px;
    line-height: 34px;
    padding-bottom: 4px;
    border-bottom: 1.5px solid var(--white);
  }
  .net-weight .kg {
    display: block;
    font-size: 20px;
    line-height: 30px;
  }
  .grade-stamp {
    position: absolute;
    left: 14px;
    top: 828px;
    width: 62px;
    height: 36px;
    background: var(--white);
    border: 2px solid var(--red);
    border-radius: 3px;
    font-family: "Oswald", sans-serif;
    font-weight: 700;
    font-size: 6px;
    line-height: 8px;
    color: var(--red);
    text-align: center;
    padding-top: 5px;
  }
</style>
</head>
<body>
<div class="canvas">
  <section class="bag-front">
    <h1 class="brand-name">Vestra Charcoal</h1>

    <p class="slogan">...light the smoke flavor</p>

    <p class="product-claim">100% Natural Hardwood Lump Charcoal</p>

    <p class="feature feature--one">No additives, No fillers, Non sparking</p>
    <p class="feature feature--two">Hi Heat, Low Ash. Long Burning</p>
    <p class="feature feature--three">Easy lighting, Mild flavor profile</p>

    <svg class="flame-band" viewBox="0 0 470 275" role="img" aria-label="Red flame decoration rising along the bottom of the bag">
      <defs>
        <linearGradient id="flameFade" x1="0" y1="0" x2="0" y2="1">
          <stop offset="0" stop-color="#ffffff"/>
          <stop offset="0.45" stop-color="#d98586"/>
          <stop offset="0.75" stop-color="#b52a2c"/>
          <stop offset="1" stop-color="#b52a2c"/>
        </linearGradient>
      </defs>
      <rect x="0" y="0" width="470" height="275" fill="url(#flameFade)"/>
    </svg>

    <div class="net-weight">
      <span class="lbs">10 LBS</span>
      <span class="kg">4.54kg</span>
    </div>

    <div class="grade-stamp">RESTAURANT<br>&amp; COMPETITION<br>GRADE</div>
  </section>
</div>
</body>
</html>
```